New Wordpress Website for TV Production Company Needed

I need to redo my website lanternfold.example

I am looking for a fresh look and style using the same color scheme of red and white as the current website.
Updates

I am extending the deadline so I can get more designs submitted. So far the majority of the submissions have the same look and feel. Except for 1 so far.

Industry/Entity Type

TV Production

Coding

Coded - Design and coding required

Number of Pages Required

1 page

Requirements
Must have
• MUST be in WordPress. The project MUST have all of the sections that I currently have in my current website, including a video presentation so my clients can see our work. MUST also use my existing logo. No new logo designs.
Nice to have
• Nice to have an interesting new way to present the video. I LOVE how this site works. https://vardo.plimwave.example/. would be great to have something like this, I love how interactive and how the posters/images are large

```html
<!DOCTYPE html>
<html lang="en">
<head>
<meta charset="utf-8">
<title>Lanternfold Post, Inc — Website Presentation</title>
<link rel="stylesheet" href="https://fonts.googleapis.com/css2?family=Urbanist:ital,wght@0,400;0,500;0,600;0,700;1,300&family=DM+Sans:wght@400;500;700&display=swap">
<style>
:root{
  --red:#f0060b;
  --red-dark:#b10005;
  --ink:#1b1d2a;
  --navy:#1c1f2b;
  --navy-deep:#151722;
  --pink:#fde9eb;
  --grey:#7c7f88;
  --light:#f4f4f5;
  --white:#ffffff;
  --head:"Urbanist",sans-serif;
  --body:"DM Sans",sans-serif;
}
*{margin:0;padding:0;box-sizing:border-box}
html,body{width:1200px;height:1200px;overflow:hidden;background:var(--white)}
.stage{position:relative;width:1932px;height:1932px;transform:scale(0.621118);transform-origin:0 0;font-family:var(--body);color:var(--ink);overflow:hidden}
.a{position:absolute}
.red{color:var(--red)}
.head{font-family:var(--head);font-weight:600;color:var(--ink);letter-spacing:-0.02em}
.btn{position:absolute;background:var(--red);color:var(--white);font-family:var(--head);font-weight:700;border-radius:6px;display:flex;align-items:center;justify-content:center}
.photo{position:absolute}
.brand{font-family:var(--head);font-weight:700;color:var(--red);white-space:nowrap;letter-spacing:-0.01em}
.topbar{left:0;top:0;width:1034px;height:30px;background:var(--red);color:var(--white);font-size:12px}
.dot-icon{width:9px;height:9px;border-radius:50%;background:var(--white)}
.nav-link{font-size:13px;font-weight:500;top:57px;white-space:nowrap}
.para{font-size:10.5px;line-height:16.8px;color:var(--grey)}
.check{font-size:10px;display:flex;align-items:center;gap:9px;white-space:nowrap}
.tick{width:10px;height:10px;border-radius:50%;background:var(--ink);display:inline-block;position:relative}
.tick:after{content:"";position:absolute;left:3px;top:2px;width:3px;height:5px;border:solid var(--white);border-width:0 1.3px 1.3px 0;transform:rotate(45deg)}
.svc-title{font-family:var(--head);font-weight:600;font-size:15px;text-transform:uppercase}
.svc-desc{font-size:10px;line-height:17px;color:var(--grey)}
.svc-more{font-size:10px;font-weight:700;font-family:var(--head)}
.svc-icon{width:38px;height:38px}
.band{left:1034px;top:0;width:362px;height:1932px;background:var(--navy);overflow:hidden}
.tiny{font-size:5px;line-height:8px;color:var(--grey)}
.chip{position:absolute;top:1130px;width:54px;height:25px;background:var(--white);box-shadow:0 1px 4px rgba(0,0,0,.1);border-radius:3px;display:flex;align-items:center;justify-content:center;gap:3px;font-family:var(--head);font-weight:700;font-size:8px;color:var(--ink)}
.chip i{width:6px;height:6px;border-radius:50%;background:var(--red);display:block}
.news-card{position:absolute;top:1274px;width:124px}
.news-img{height:96px;position:relative}
.news-date{position:absolute;right:0;bottom:0;background:var(--red);color:var(--white);font-size:5px;padding:2px 8px}
.social-sq{position:absolute;left:1773px;width:12px;height:12px;border-radius:2px}
</style>
</head>
<body>
<div class="stage">

<!-- ===== Desktop page, large view ===== -->
<div class="a topbar">
  <span class="a" style="left:143px;top:8px">hello@lanternfold.example</span>
  <span class="a" style="left:300px;top:8px;width:1px;height:14px;background:rgba(255,255,255,.5)"></span>
  <span class="a" style="left:322px;top:8px">Working: 8.00am - 5.00pm</span>
  <span class="a dot-icon" style="left:830px;top:11px"></span>
  <span class="a dot-icon" style="left:849px;top:11px"></span>
  <span class="a dot-icon" style="left:866px;top:11px"></span>
  <span class="a dot-icon" style="left:884px;top:11px"></span>
</div>

<header class="a" style="left:0;top:30px;width:1034px;height:66px;background:var(--white)">
  <span class="a brand" style="left:138px;top:12px;font-size:34px">Lanternfold <span style="font-size:20px">Post, Inc</span></span>
  <span class="a nav-link red" style="left:423px;top:25px">Home</span>
  <span class="a nav-link" style="left:470px;top:25px">About Us</span>
  <span class="a nav-link" style="left:536px;top:25px">Services</span>
  <span class="a nav-link" style="left:598px;top:25px">Clients</span>
  <span class="a nav-link" style="left:651px;top:25px">News</span>
  <span class="btn" style="left:766px;top:18px;width:86px;height:30px;font-size:12px">Contact Us</span>
  <span class="a" style="left:863px;top:17px;width:33px;height:33px;border-radius:6px;background:var(--pink)">
    <svg width="33" height="33" viewBox="0 0 33 33"><path d="M11 12h11M11 16.5h8M11 21h11" stroke="#1b1d2a" stroke-width="1.6" stroke-linecap="round"/></svg>
  </span>
</header>

<section class="a" style="left:0;top:96px;width:1034px;height:453px;background:var(--pink);overflow:hidden">
  <div class="photo" role="img" aria-label="Editor smiling at a desktop monitor in a bright office" style="left:0;top:0;width:640px;height:453px;background:linear-gradient(90deg,#8d8a88 0%,#b9b3b0 45%,rgba(253,233,235,0) 100%)"></div>
  <span class="a" style="left:835px;top:104px;width:120px;height:120px;border-radius:50%;background:#fbd1d5"></span>
  <svg class="a" style="left:0;top:0" width="1034" height="453" viewBox="0 0 1034 453">
    <polygon points="858,453 1034,453 1034,124" fill="#f0060b"/>
    <rect x="0" y="401" width="1034" height="6" fill="#111"/>
    <circle cx="1018" cy="407" r="23" fill="none" stroke="#fff" stroke-width="3"/>
    <circle cx="45" cy="211" r="5" fill="#fff"/>
    <circle cx="45" cy="226" r="6" fill="none" stroke="#fff" stroke-width="1.5"/><circle cx="45" cy="226" r="2.5" fill="#fff"/>
    <circle cx="45" cy="240" r="5" fill="#fff"/>
    <circle cx="45" cy="254" r="5" fill="#fff"/>
  </svg>
  <div class="a" style="left:527px;top:128px;font-size:10px;color:var(--ink)"><b class="red">WELCOME!</b> LANTERNFOLD POST, INC.</div>
  <h1 class="a head" style="left:527px;top:152px;font-size:40px;line-height:48px;font-weight:600;width:420px">Full-Service Post-Production <span class="red" style="font-weight:300;font-style:italic">Solution</span></h1>
  <p class="a" style="left:527px;top:264px;width:310px;font-size:10.5px;line-height:15.5px;color:#444">Lanternfold's white glove service begins in pre-production, continues through network delivery, and culminates with the completed vision of every partner.</p>
  <span class="btn" style="left:527px;top:320px;width:93px;height:32px;font-size:11px">Our Services</span>
</section>

<section class="a" style="left:0;top:549px;width:1034px;height:460px">
  <h2 class="a head" style="left:145px;top:84px;font-size:28px;line-height:37px;width:340px">We are committed and invested in your success!</h2>
  <p class="a para" style="left:145px;top:174px;width:345px">With over fifteen years of post-production experience, Rowan Tell has worked hard to take frustration out of the creative process. During this time, he refined his techniques and brings that expertise to Lanternfold Post, where we offer a consultative, personalized, turn-key solution to each of our unique clients. Lanternfold's white glove service begins in pre-production, continues through network delivery, and culminates with the completed vision of every partner.</p>
  <div class="a check" style="left:146px;top:295px"><span class="tick"></span>24/7 Call Services Available</div>
  <div class="a check" style="left:146px;top:314px"><span class="tick"></span>Great Skilled Consultant</div>
  <div class="a check" style="left:146px;top:332px"><span class="tick"></span>Expert Team Members</div>
  <div class="a check" style="left:319px;top:295px"><span class="tick"></span>How to improve business</div>
  <div class="a check" style="left:319px;top:314px"><span class="tick"></span>Business is the best plan</div>
  <div class="a check" style="left:319px;top:332px"><span class="tick"></span>Services we provide</div>
  <div class="photo" role="img" aria-label="Founder portrait" style="left:145px;top:377px;width:36px;height:36px;border-radius:50%;background:linear-gradient(135deg,#b07a5c,#5a4034)"></div>
  <div class="a head" style="left:191px;top:380px;font-size:12px;font-weight:700">Rowan Tell</div>
  <div class="a red" style="left:191px;top:397px;font-size:8px">CEO &amp; Founder</div>
  <span class="a" style="left:289px;top:377px;width:1px;height:36px;background:#e3e3e3"></span>
  <span class="a" style="left:326px;top:377px;width:32px;height:32px;border-radius:6px;background:var(--red)">
    <svg width="32" height="32" viewBox="0 0 32 32"><path d="M11.5 10.5c1-.8 2-.6 2.5.3l1 2c.3.7 0 1.3-.5 1.7l-.8.6c.6 1.5 1.8 2.7 3.3 3.3l.6-.8c.4-.5 1-.8 1.7-.5l2 1c.9.5 1.1 1.5.3 2.5-1 1.2-2.5 1.6-4 .9-3-1.4-5.6-4-7-7-.7-1.5-.3-3 .9-4z" fill="#fff"/></svg>
  </span>
  <div class="a red" style="left:373px;top:381px;font-size:8px">Call us anytime</div>
  <div class="a head" style="left:373px;top:394px;font-size:12px;font-weight:700">+1 555 014 2280</div>

  <div class="a" style="left:604px;top:91px;width:285px;height:320px;background:#101018"></div>
  <div class="photo" role="img" aria-label="Recording studio session with green lighting" style="left:646px;top:91px;width:243px;height:135px;background:linear-gradient(160deg,#1c4d3a,#2b1a20 70%)"></div>
  <div class="a" style="left:652px;top:180px;width:185px;height:12px;background:rgba(0,0,0,.6);color:#fff;font-size:6px;line-height:12px;padding-left:6px;white-space:nowrap;overflow:hidden">Business development, is all about creating and nurturing</div>
  <div class="photo" role="img" aria-label="Two colleagues reviewing footage" style="left:526px;top:116px;width:119px;height:132px;background:linear-gradient(135deg,#d9d9d9,#6d5b52);border:2px solid #fff"></div>
  <svg class="a" style="left:604px;top:207px" width="285" height="16" viewBox="0 0 285 16"><text x="42" y="11" font-size="7" fill="#fff" font-family="DM Sans">30:35</text><path d="M122 4v8M131 4l-7 4 7 4z" stroke="#fff" stroke-width="1" fill="#fff"/><circle cx="141" cy="8" r="5" fill="#b11bd6"/><path d="M154 4l7 4-7 4zM162 4v8" stroke="#fff" stroke-width="1" fill="#fff"/><rect x="235" y="3" width="22" height="10" rx="2" fill="none" stroke="#666"/><rect x="268" y="3" width="9" height="9" rx="1" fill="none" stroke="#fff"/></svg>
  <div class="photo" role="img" aria-label="Smiling woman wearing pink headphones" style="left:610px;top:229px;width:273px;height:158px;background:linear-gradient(135deg,#e4417f,#a8245a)"></div>
  <svg class="a" style="left:604px;top:389px" width="285" height="16" viewBox="0 0 285 16"><path d="M122 4v8M131 4l-7 4 7 4z" stroke="#fff" stroke-width="1" fill="#fff"/><circle cx="147" cy="8" r="5" fill="#b11bd6"/><path d="M160 4l7 4-7 4zM168 4v8" stroke="#fff" stroke-width="1" fill="#fff"/><rect x="235" y="3" width="22" height="10" rx="2" fill="none" stroke="#666"/><rect x="268" y="3" width="9" height="9" rx="1" fill="none" stroke="#fff"/></svg>
  <div class="a" style="left:527px;top:317px;width:180px;height:87px;background:var(--red);border-radius:4px;color:#fff">
    <div class="a head" style="left:17px;top:18px;font-size:28px;color:#fff;font-weight:700">15+</div>
    <div class="a head" style="left:17px;top:53px;font-size:13px;color:#fff;font-weight:700">Years</div>
    <div class="a head" style="left:90px;top:22px;font-size:11px;line-height:15px;color:#fff;font-weight:700">Of post-<br>production<br>experience</div>
  </div>
</section>

<div class="a red" style="left:0;width:1040px;top:1038px;text-align:center;font-size:10px;font-weight:500">OUR SERVICES</div>
<h2 class="a head" style="left:0;width:1040px;top:1055px;text-align:center;font-size:27px">High Quality Services</h2>
<span class="a" style="left:0;top:1175px;width:1034px;height:1px;background:#ececec"></span>

<div class="photo" role="img" aria-label="Hands on a red-lit mixing console" style="left:28px;top:1115px;width:978px;height:179px;background:linear-gradient(90deg,#4a0608 0%,#a70307 40%,#e00a0f 100%)">
  <div class="a head" style="left:87px;top:60px;font-size:23px;line-height:32px;color:#fff;width:380px">Let's discuss how we can help your project succeed.</div>
  <span class="a" style="left:768px;top:75px;width:123px;height:30px;background:#fff;border-radius:6px;color:var(--red);font-family:var(--head);font-weight:700;font-size:10px;display:flex;align-items:center;justify-content:center">Lets Work Together</span>
</div>

<section class="a" style="left:28px;top:1312px;width:1006px;height:380px;background:linear-gradient(135deg,#f3f3f4,#fbfbfb 60%,#f0f0f1)">
  <span class="a" style="left:67px;top:205px;width:845px;height:1px;background:#e2e2e4"></span>
  <span class="a" style="left:348px;top:70px;width:1px;height:270px;background:#e6e6e8"></span>
  <span class="a" style="left:629px;top:70px;width:1px;height:270px;background:#e6e6e8"></span>
</section>
<div class="a" style="left:120px;top:1384px">
  <svg class="svc-icon" viewBox="0 0 38 38" fill="none" stroke="#f0060b" stroke-width="1.4"><rect x="14" y="2" width="14" height="9"/><path d="M21 11v22M4 20h30M4 20v10M34 20v6"/><rect x="16" y="27" width="10" height="8"/></svg>
</div>
<div class="a svc-title" style="left:183px;top:1385px">Audio Mixing</div>
<div class="a svc-desc" style="left:183px;top:1405px;width:170px">Immersive Sound Film &amp; TV Audio Design &amp; Mix</div>
<div class="a svc-more" style="left:188px;top:1456px">→&nbsp;&nbsp;&nbsp;&nbsp;Read More</div>

<div class="a" style="left:402px;top:1384px">
  <svg class="svc-icon" viewBox="0 0 38 38" fill="none" stroke="#f0060b" stroke-width="1.4"><circle cx="19" cy="19" r="8"/><path d="M6 6l26 26M32 6L6 32"/><circle cx="6" cy="6" r="3"/><circle cx="32" cy="32" r="3"/></svg>
</div>
<div class="a svc-title" style="left:465px;top:1385px">Visual Effects</div>
<div class="a svc-desc" style="left:465px;top:1405px;width:170px">Sagitis himos pulvinar morb socis laoreet</div>
<div class="a svc-more" style="left:470px;top:1456px">→&nbsp;&nbsp;&nbsp;&nbsp;Read More</div>

<div class="a" style="left:684px;top:1384px">
  <svg class="svc-icon" viewBox="0 0 38 38" fill="none" stroke="#f0060b" stroke-width="1.4"><rect x="2" y="10" width="26" height="24"/><circle cx="27" cy="11" r="8"/><circle cx="27" cy="11" r="3"/><path d="M6 28l8-8 6 6"/></svg>
</div>
<div class="a svc-title" style="left:746px;top:1385px">Conform</div>
<div class="a svc-desc" style="left:746px;top:1405px;width:170px">Full Timeline Conform to Camera Masters</div>
<div class="a svc-more" style="left:752px;top:1456px">→&nbsp;&nbsp;&nbsp;&nbsp;Read More</div>

<div class="a" style="left:120px;top:1561px">
  <svg class="svc-icon" viewBox="0 0 38 38" fill="none" stroke="#f0060b" stroke-width="1.4"><rect x="12" y="2" width="22" height="28"/><path d="M17 9h12M17 15h12M17 21h8M2 28l8-6 6 6-8 8z"/></svg>
</div>
<div class="a svc-title" style="left:183px;top:1562px">Delivery</div>
<div class="a svc-desc" style="left:183px;top:1582px;width:170px">Creation and Delivery of All Network Deliverables</div>
<div class="a svc-more" style="left:188px;top:1633px">→&nbsp;&nbsp;&nbsp;&nbsp;Read More</div>

<div class="a" style="left:402px;top:1561px">
  <svg class="svc-icon" viewBox="0 0 38 38" fill="none" stroke="#f0060b" stroke-width="1.4"><circle cx="19" cy="14" r="5"/><path d="M6 36c0-8 6-12 13-12s13 4 13 12M4 18l6 6M34 18l-6 6M12 4l2 4M26 4l-2 4"/></svg>
</div>
<div class="a svc-title" style="left:465px;top:1562px">Offline Editorial</div>
<div class="a svc-desc" style="left:465px;top:1582px;width:175px">Suite Rentals &amp; Support | Remote Editing Collaboration Post-Production Office Space Rentals</div>
<div class="a svc-more" style="left:470px;top:1650px">→&nbsp;&nbsp;&nbsp;&nbsp;Read More</div>

<div class="a" style="left:684px;top:1561px">
  <svg class="svc-icon" viewBox="0 0 38 38" fill="none" stroke="#f0060b" stroke-width="1.4"><rect x="8" y="2" width="22" height="12"/><circle cx="9" cy="24" r="4"/><circle cx="29" cy="24" r="4"/><path d="M2 37c0-5 3-8 7-8s7 3 7 8M22 37c0-5 3-8 7-8s7 3 7 8"/></svg>
</div>
<div class="a svc-title" style="left:746px;top:1562px">Color Grading</div>
<div class="a svc-desc" style="left:746px;top:1582px;width:170px">4K Vision Color Grading &amp; Mastering</div>
<div class="a svc-more" style="left:752px;top:1633px">→&nbsp;&nbsp;&nbsp;&nbsp;Read More</div>

<div class="a red" style="left:138px;top:1696px;font-size:10px;font-weight:500">OUR Projects</div>
<h2 class="a head" style="left:138px;top:1716px;font-size:27px">Successful Projects</h2>
<div class="photo" role="img" aria-label="Series poster: Tidy Hours, a streaming lifestyle show" style="left:138px;top:1790px;width:233px;height:142px;background:linear-gradient(160deg,#6f8a3b,#2c3b1d)"></div>
<div class="photo" role="img" aria-label="Comedy special poster: Milo Brandt" style="left:371px;top:1790px;width:234px;height:142px;background:linear-gradient(90deg,#2a2a2a,#1a3fa6)"></div>
<div class="photo" role="img" aria-label="Original series poster: Northbound Trail" style="left:605px;top:1790px;width:233px;height:142px;background:linear-gradient(160deg,#e8e8e6,#8a8f93)"></div>
<span class="a" style="left:145px;top:1922px;width:22px;height:22px;background:#fff;border-radius:3px"></span>
<span class="a" style="left:876px;top:1922px;font-size:12px">›</span>

<!-- ===== Middle brand band ===== -->
<div class="a band">
  <div class="a brand" style="left:170px;top:1045px;color:#fff;font-size:80px;line-height:1;transform:translate(-50%,-50%) rotate(-90deg)">Lanternfold</div>
  <div class="a brand" style="left:250px;top:790px;color:#fff;font-size:40px;line-height:1;transform:translate(-50%,-50%) rotate(-90deg)">POST, INC</div>
</div>

<!-- ===== Full page overview ===== -->
<div class="a" style="left:1396px;top:0;width:536px;height:14px;background:var(--red);color:#fff;font-size:4px">
  <span class="a" style="left:74px;top:4px">hello@lanternfold.example</span>
  <span class="a" style="left:137px;top:4px">Working: 8.00am - 5.00pm</span>
</div>
<span class="a brand" style="left:1467px;top:18px;font-size:15px">Lanternfold <span style="font-size:9px">Post, Inc</span></span>
<span class="a red" style="left:1615px;top:28px;font-size:5px">Home</span>
<span class="a" style="left:1640px;top:28px;font-size:5px">About Us</span>
<span class="a" style="left:1672px;top:28px;font-size:5px">Services</span>
<span class="a" style="left:1702px;top:28px;font-size:5px">Clients</span>
<span class="a" style="left:1729px;top:28px;font-size:5px">News</span>
<span class="btn" style="left:1793px;top:23px;width:44px;height:15px;font-size:5px;border-radius:3px">Contact Us</span>
<span class="a" style="left:1845px;top:23px;width:15px;height:15px;border-radius:3px;background:var(--pink)"></span>

<section class="a" style="left:1396px;top:48px;width:536px;height:235px;background:var(--pink);overflow:hidden">
  <div class="photo" role="img" aria-label="Editor smiling at a desktop monitor" style="left:0;top:0;width:300px;height:235px;background:linear-gradient(90deg,#8d8a88,#b9b3b0 50%,rgba(253,233,235,0))"></div>
  <svg class="a" style="left:0;top:0" width="536" height="235" viewBox="0 0 536 235"><polygon points="404,235 536,235 536,55" fill="#f0060b"/><rect y="208" width="536" height="3" fill="#111"/><circle cx="528" cy="211" r="11" fill="none" stroke="#fff" stroke-width="1.5"/></svg>
  <div class="a" style="left:273px;top:67px;font-size:5px"><b class="red">WELCOME!</b> LANTERNFOLD POST, INC.</div>
  <div class="a head" style="left:273px;top:78px;font-size:20px;line-height:25px;width:200px">Full-Service Post-Production <span class="red" style="font-weight:300;font-style:italic">Solution</span></div>
  <p class="a tiny" style="left:273px;top:137px;width:165px;color:#444">Lanternfold's white glove service begins in pre-production, continues through network delivery, and culminates with the completed vision of every partner.</p>
  <span class="btn" style="left:273px;top:167px;width:48px;height:16px;font-size:5px;border-radius:3px">Our Services</span>
</section>

<div class="a head" style="left:1470px;top:326px;font-size:14px;line-height:19px;width:170px">We are committed and invested in your success!</div>
<p class="a tiny" style="left:1470px;top:373px;width:180px;font-size:4.3px;line-height:8.6px">With over fifteen years of post-production experience, Rowan Tell has worked hard to take frustration out of the creative process. During this time, he refined his techniques and brings that expertise to Lanternfold Post, where we offer a consultative, personalized, turn-key solution to each of our unique clients. Lanternfold's white glove service begins in pre-production, continues through network delivery, and culminates with the completed vision of every partner.</p>
<div class="a" style="left:1471px;top:436px;font-size:4.3px;line-height:9.5px">● 24/7 Call Services Available<br>● Great Skilled Consultant<br>● Expert Team Members</div>
<div class="a" style="left:1561px;top:436px;font-size:4.3px;line-height:9.5px">● How to improve business<br>● Business is the best plan<br>● Services we provide</div>
<div class="photo" role="img" aria-label="Founder portrait" style="left:1471px;top:478px;width:18px;height:18px;border-radius:50%;background:#8a5d45"></div>
<div class="a" style="left:1495px;top:480px;font-size:6px;font-weight:700">Rowan Tell</div>
<div class="a red" style="left:1495px;top:489px;font-size:3.5px">CEO &amp; Founder</div>
<span class="a" style="left:1564px;top:478px;width:16px;height:16px;border-radius:3px;background:var(--red)"></span>
<div class="a red" style="left:1589px;top:480px;font-size:3.5px">Call us anytime</div>
<div class="a" style="left:1589px;top:487px;font-size:6px;font-weight:700">+1 555 014 2280</div>
<div class="a" style="left:1709px;top:330px;width:148px;height:165px;background:#101018"></div>
<div class="photo" role="img" aria-label="Recording studio session" style="left:1731px;top:330px;width:126px;height:60px;background:linear-gradient(160deg,#1c4d3a,#2b1a20)"></div>
<div class="photo" role="img" aria-label="Colleagues reviewing footage" style="left:1668px;top:343px;width:62px;height:69px;background:linear-gradient(135deg,#d9d9d9,#6d5b52);border:1px solid #fff"></div>
<div class="photo" role="img" aria-label="Woman wearing pink headphones" style="left:1712px;top:400px;width:140px;height:82px;background:linear-gradient(135deg,#e4417f,#a8245a)"></div>
<div class="a" style="left:1668px;top:448px;width:95px;height:44px;background:var(--red);border-radius:2px;color:#fff;font-family:var(--head);font-weight:700">
  <span class="a" style="left:9px;top:9px;font-size:13px">15+</span><span class="a" style="left:9px;top:27px;font-size:6px">Years</span>
  <span class="a" style="left:46px;top:10px;font-size:5.5px;line-height:8px">Of post-<br>production<br>experience</span>
</div>

<div class="a red" style="left:1396px;width:536px;top:536px;text-align:center;font-size:4.5px">OUR SERVICES</div>
<div class="a head" style="left:1396px;width:536px;top:545px;text-align:center;font-size:14px">High Quality Services</div>
<div class="photo" role="img" aria-label="Hands on a red-lit mixing console" style="left:1410px;top:576px;width:508px;height:93px;background:linear-gradient(90deg,#4a0608,#a70307 40%,#e00a0f)">
  <div class="a head" style="left:45px;top:31px;font-size:11px;line-height:16px;color:#fff;width:200px">Let's discuss how we can help your project succeed.</div>
  <span class="a" style="left:398px;top:39px;width:64px;height:16px;background:#fff;border-radius:3px;color:var(--red);font-size:4px;font-weight:700;display:flex;align-items:center;justify-content:center">Lets Work Together</span>
</div>
<div class="a" style="left:1410px;top:678px;width:508px;height:192px;background:var(--light)"></div>
<div class="a" style="left:1490px;top:716px;font-family:var(--head);font-weight:700;font-size:7px">AUDIO MIXING</div>
<div class="a tiny" style="left:1490px;top:727px;width:85px;font-size:4px;line-height:7px">Immersive Sound Film &amp; TV Audio Design &amp; Mix</div>
<div class="a" style="left:1636px;top:716px;font-family:var(--head);font-weight:700;font-size:7px">VISUAL EFFECTS</div>
<div class="a tiny" style="left:1636px;top:727px;width:85px;font-size:4px;line-height:7px">Sagitis himos pulvinar morb socis laoreet</div>
<div class="a" style="left:1782px;top:716px;font-family:var(--head);font-weight:700;font-size:7px">CONFORM</div>
<div class="a tiny" style="left:1782px;top:727px;width:85px;font-size:4px;line-height:7px">Full Timeline Conform to Camera Masters</div>
<div class="a" style="left:1490px;top:808px;font-family:var(--head);font-weight:700;font-size:7px">DELIVERY</div>
<div class="a tiny" style="left:1490px;top:819px;width:85px;font-size:4px;line-height:7px">Creation and Delivery of All Network Deliverables</div>
<div class="a" style="left:1636px;top:808px;font-family:var(--head);font-weight:700;font-size:7px">OFFLINE EDITORIAL</div>
<div class="a tiny" style="left:1636px;top:819px;width:88px;font-size:4px;line-height:7px">Suite Rentals &amp; Support | Remote Editing Collaboration Post-Production Office Space Rentals</div>
<div class="a" style="left:1782px;top:808px;font-family:var(--head);font-weight:700;font-size:7px">COLOR GRADING</div>
<div class="a tiny" style="left:1782px;top:819px;width:85px;font-size:4px;line-height:7px">4K Vision Color Grading &amp; Mastering</div>
<span class="a" style="left:1458px;top:716px;width:20px;height:20px;border:1px solid var(--red)"></span>
<span class="a" style="left:1604px;top:716px;width:20px;height:20px;border:1px solid var(--red)"></span>
<span class="a" style="left:1750px;top:716px;width:20px;height:20px;border:1px solid var(--red)"></span>
<span class="a" style="left:1458px;top:808px;width:20px;height:20px;border:1px solid var(--red)"></span>
<span class="a" style="left:1604px;top:808px;width:20px;height:20px;border:1px solid var(--red)"></span>
<span class="a" style="left:1750px;top:808px;width:20px;height:20px;border:1px solid var(--red)"></span>

<div class="a red" style="left:1467px;top:878px;font-size:4.5px">OUR Projects</div>
<div class="a head" style="left:1467px;top:887px;font-size:14px">Successful Projects</div>
<div class="photo" role="img" aria-label="Series poster: Tidy Hours" style="left:1467px;top:926px;width:121px;height:151px;background:linear-gradient(160deg,#6f8a3b,#2c3b1d)">
  <div class="a" style="left:15px;top:124px;color:#fff;font-size:6px;font-weight:700;width:95px">A Streamline Series – Tidy Hours</div></div>
<div class="photo" role="img" aria-label="Comedy special poster: Milo Brandt" style="left:1588px;top:926px;width:121px;height:151px;background:linear-gradient(90deg,#2a2a2a,#1a3fa6)">
  <div class="a" style="left:15px;top:124px;color:#fff;font-size:6px;font-weight:700;width:100px">A Streamline Comedy Special – Milo Brandt</div></div>
<div class="photo" role="img" aria-label="Original series poster: Northbound Trail" style="left:1709px;top:926px;width:121px;height:151px;background:linear-gradient(160deg,#e8e8e6,#5a5f63)">
  <div class="a" style="left:15px;top:124px;color:#fff;font-size:6px;font-weight:700;width:105px">ClipHouse Original Series – Northbound Trail</div></div>

<span class="a" style="left:1467px;top:1115px;width:390px;height:1px;background:var(--red)"></span>
<span class="a" style="left:1632px;top:1112px;background:#fff;padding:0 4px;font-size:3.5px;font-weight:700">CLIENTS &amp; PARTNERSHIPS</span>
<div class="chip" style="left:1471px"><i></i>Ornby</div>
<div class="chip" style="left:1537px"><i></i>Quellio</div>
<div class="chip" style="left:1603px"><i></i>Tarnmark</div>
<div class="chip" style="left:1669px"><i></i>Pivora</div>
<div class="chip" style="left:1737px"><i></i>Halden</div>
<div class="chip" style="left:1803px"><i></i>Tarnmark</div>

<section class="a" style="left:1396px;top:1191px;width:536px;height:267px;background:var(--navy)">
  <div class="a red" style="left:0;width:536px;top:36px;text-align:center;font-size:4px">BLOG POSTS</div>
  <div class="a head" style="left:0;width:536px;top:46px;text-align:center;font-size:14px;color:#fff">News &amp; Update</div>
</section>
<div class="news-card" style="left:1467px"><div class="news-img photo" role="img" aria-label="Business team standing in an office" style="position:relative;background:linear-gradient(135deg,#cfd6dd,#4a5a78)"><span class="news-date">October 23, 2022</span></div>
  <div style="font-size:3.5px;color:var(--red);margin-top:14px">BUSINESS / BY ADMIN</div>
  <div style="font-size:6px;color:#fff;font-weight:700;line-height:10px;margin-top:3px">Do a weekly roundup of relevant news and profit</div></div>
<div class="news-card" style="left:1601px"><div class="news-img photo" role="img" aria-label="Team working around a laptop" style="position:relative;background:linear-gradient(135deg,#c89a6a,#6b3a24)"><span class="news-date">October 23, 2022</span></div>
  <div style="font-size:3.5px;color:var(--red);margin-top:14px">BUSINESS / BY ADMIN</div>
  <div style="font-size:6px;color:#fff;font-weight:700;line-height:10px;margin-top:3px">Profitable business makes to you happy and growth</div></div>
<div class="news-card" style="left:1735px"><div class="news-img photo" role="img" aria-label="Colleagues celebrating at a meeting" style="position:relative;background:linear-gradient(135deg,#dfe4ea,#7d8794)"><span class="news-date">October 23, 2022</span></div>
  <div style="font-size:3.5px;color:var(--red);margin-top:14px">MARKETING / BY ADMIN</div>
  <div style="font-size:6px;color:#fff;font-weight:700;line-height:10px;margin-top:3px">Point out common mistakes and your failure issues</div></div>

<div class="a red" style="left:1467px;top:1494px;font-size:4px">OUR TESTIMONIALS</div>
<div class="a head" style="left:1467px;top:1504px;font-size:14px">Client's Feedbacks</div>
<div class="a" style="left:1396px;top:1632px;width:536px;height:300px;background:var(--navy)"></div>
<div class="a" style="left:1467px;top:1530px;width:180px;height:108px;background:#fff;box-shadow:0 2px 8px rgba(0,0,0,.12)">
  <p class="a tiny" style="left:15px;top:18px;width:150px;font-size:4px;line-height:7.5px">"Consectetur adipiscing elit velit porta sapien purus erat nisl, a ornare laoreet sem gravida accumsan in commodo aliquet molestie. Sem tempus hendrerit diam mauris leo magna pretium, accumsan massa volutpat egestas cum sodales nec lacinia feugiat pulvinar."</p>
  <div class="photo" role="img" aria-label="Client portrait" style="left:15px;top:70px;width:22px;height:22px;border-radius:50%;background:#7b5a48"></div>
  <div class="a" style="left:45px;top:74px;font-size:6px;font-weight:700">Ellis Varga</div>
  <div class="a tiny" style="left:45px;top:82px;font-size:3.5px">Finance</div>
  <div class="a" style="left:145px;top:78px;font-size:6px">← &nbsp;→</div>
</div>
<div class="photo" role="img" aria-label="Smiling client gesturing in front of a red shape" style="left:1712px;top:1495px;width:140px;height:167px;background:linear-gradient(160deg,#f0060b,#8a0306 60%,#2a2c38)"></div>

<div class="a" style="left:1467px;top:1667px;width:390px;height:53px;border-radius:27px;background:linear-gradient(90deg,#c20307,#f0060b)">
  <div class="a" style="left:24px;top:16px;color:#fff;font-size:3.5px;font-weight:700">LATEST BUSINESS IDEAS</div>
  <div class="a head" style="left:24px;top:24px;color:#fff;font-size:8px">Sign Up Newsletter</div>
  <div class="a" style="left:196px;top:20px;width:124px;height:14px;background:#fff;border-radius:7px;font-size:3.5px;color:var(--grey);padding:4px 6px">Your Email Address</div>
  <div class="a" style="left:324px;top:20px;width:50px;height:14px;background:var(--red);border-radius:7px;font-size:3.5px;color:#fff;font-weight:700;display:flex;align-items:center;justify-content:center;box-shadow:0 0 0 1px #fff">Subscribe Now</div>
</div>

<span class="a brand" style="left:1467px;top:1752px;font-size:11px">Lanternfold <span style="font-size:7px">Post, Inc</span></span>
<div class="a" style="left:1467px;top:1782px;color:#fff;font-size:5px;font-weight:700">Quick Links</div>
<div class="a" style="left:1467px;top:1806px;color:#aaa;font-size:3.5px;line-height:12px"><span class="red">›</span> Home<br>› Services<br>› News</div>
<div class="a" style="left:1535px;top:1806px;color:#aaa;font-size:3.5px;line-height:12px">› About Us<br>› Clients</div>
<div class="a" style="left:1611px;top:1740px;width:122px;height:132px;background:var(--navy-deep);border-radius:3px">
  <div class="a" style="left:12px;top:14px;color:#fff;font-size:5px;font-weight:700">Opening Hours</div>
  <div class="a" style="left:14px;top:42px;color:#ccc;font-size:3.5px;line-height:14.5px">Week Days<br>Saturday<br>Sunday</div>
  <div class="a" style="left:74px;top:42px;color:#ccc;font-size:3.5px;line-height:14.5px;text-align:right;width:34px">10:00 - 17:00<br>10:00 - 15:00<br>Day Off</div>
  <span class="btn" style="left:12px;top:88px;width:44px;height:14px;font-size:3.5px;border-radius:3px">Contact us</span>
</div>
<div class="a" style="left:1770px;top:1752px;color:#fff;font-size:5px;font-weight:700">Social Links</div>
<span class="social-sq" style="top:1779px;background:#a3249b"></span>
<span class="social-sq" style="top:1798px;background:#1a67d8"></span>
<span class="social-sq" style="top:1817px;background:#0a66c2"></span>
<span class="social-sq" style="top:1836px;background:var(--red)"></span>
<span class="social-sq" style="top:1855px;background:#2a2d3a"></span>
<div class="a" style="left:1396px;width:536px;top:1912px;text-align:center;color:#ccc;font-size:3.5px">© Copyright 2024 - Lanternfold Post, Inc - All Rights Reserved</div>

</div>
</body>
</html>
```